Packaging for a new tea company

Hi guys we need a new packaging design for a tea company we are starting

Our competitors are leafara, zo ren tea

I have uploaded pictures of our competitors for you to see the sample
The label need to be catchy

Our brand is called #PlumVexaTea
We need two packaging designs one for Day Tea and one for calmora

Detox - slim - cleanse

Also needs to says 14 Day Orvalin

Target Market(s)

Young people

Industry/Entity Type

It Company

Colors
000000

Requirements
Must have
• #plumvexatea
Nice to have
• Herbal tea supplement 50gram
• Max label size 13.5cm x 16.5 cm
• Personally I like the paper brown bag as it looks like a higher quality and as the label is a sticker I think this would make the product look a lot better
Should not have
• Nothing

```html
<!DOCTYPE html>
<html lang="en">
<head>
<meta charset="utf-8">
<title>#PlumVexaTea – 14 Day Orvalin</title>
<link rel="stylesheet" href="https://fonts.googleapis.com/css2?family=Londrina+Solid:wght@400;900&family=Pathway+Gothic+One&display=swap">
<style>
  :root {
    --backdrop: #84f9cf;
    --kraft: #c9a070;
    --kraft-seam: #b48a5c;
    --paper-white: #efefef;
    --ink-black: #111111;
  }
  html, body {
    margin: 0;
    padding: 0;
    width: 1200px;
    height: 899px;
    overflow: hidden;
  }
  body {
    background: var(--backdrop);
    position: relative;
  }
  .pouch {
    position: absolute;
    top: 207px;
    width: 343px;
    height: 507px;
    border-radius: 0 0 14px 14px;
    overflow: hidden;
  }
  .pouch--day { left: 160px; background: var(--paper-white); color: var(--ink-black); }
  .pouch--night { left: 735px; background: var(--ink-black); color: var(--paper-white); }
  .pouch__seal {
    position: absolute;
    left: 0; top: 0;
    width: 100%;
    height: 69px;
    background: var(--kraft);
    border-bottom: 3px solid var(--kraft-seam);
  }
  .pouch__seal::after {
    content: "";
    position: absolute;
    left: 0; right: 0; top: 58px;
    height: 2px;
    background: var(--kraft-seam);
  }
  .pouch__brand {
    position: absolute;
    top: 100px;
    width: 100%;
    text-align: center;
    font-family: "Londrina Solid", sans-serif;
    font-weight: 900;
    font-size: 34px;
    letter-spacing: 1px;
    margin: 0;
  }
  .label-disc {
    position: absolute;
    left: 53px;
    top: 170px;
    width: 237px;
    height: 237px;
    border-radius: 50%;
    display: flex;
    flex-direction: column;
    align-items: center;
    justify-content: center;
  }
  .pouch--day .label-disc { background: var(--ink-black); color: var(--paper-white); }
  .pouch--night .label-disc { background: var(--paper-white); color: var(--ink-black); }
  .label-disc__title {
    font-family: "Londrina Solid", sans-serif;
    font-weight: 900;
    font-size: 56px;
    line-height: 58px;
    text-align: center;
    margin: 10px 0 4px;
  }
  .label-disc__icon { width: 30px; height: 30px; }
  .pouch__descriptor {
    position: absolute;
    top: 430px;
    width: 100%;
    text-align: center;
    font-family: "Pathway Gothic One", sans-serif;
    font-size: 17px;
    letter-spacing: 1.5px;
    text-transform: uppercase;
    margin: 0;
  }
  .pouch__weight {
    position: absolute;
    top: 476px;
    width: 100%;
    text-align: center;
    font-family: "Pathway Gothic One", sans-serif;
    font-size: 13px;
    margin: 0;
  }
</style>
</head>
<body>
  <section class="pouch pouch--day" aria-label="Day tea pouch">
    <div class="pouch__seal"></div>
    <h1 class="pouch__brand">#PlumVexaTea</h1>
    <div class="label-disc">
      <p class="label-disc__title">14 day<br>Orvalin</p>
      <svg class="label-disc__icon" viewBox="0 0 30 30" aria-label="Sun">
        <g stroke="currentColor" stroke-width="2" stroke-linecap="round">
          <line x1="15" y1="2" x2="15" y2="6"/><line x1="15" y1="24" x2="15" y2="28"/>
          <line x1="2" y1="15" x2="6" y2="15"/><line x1="24" y1="15" x2="28" y2="15"/>
          <line x1="6" y1="6" x2="8.5" y2="8.5"/><line x1="21.5" y1="21.5" x2="24" y2="24"/>
          <line x1="24" y1="6" x2="21.5" y2="8.5"/><line x1="8.5" y1="21.5" x2="6" y2="24"/>
        </g>
        <circle cx="15" cy="15" r="6" fill="currentColor"/>
      </svg>
    </div>
    <p class="pouch__descriptor">Herbal tea supplement</p>
    <p class="pouch__weight">50G</p>
  </section>

  <section class="pouch pouch--night" aria-label="Night tea pouch">
    <div class="pouch__seal"></div>
    <h2 class="pouch__brand">#PlumVexaTea</h2>
    <div class="label-disc">
      <p class="label-disc__title">14 day<br>Orvalin</p>
      <svg class="label-disc__icon" viewBox="0 0 30 30" aria-label="Crescent moon">
        <path d="M19 4 A11 11 0 1 0 24 24 A9 9 0 0 1 19 4 Z" fill="currentColor"/>
      </svg>
    </div>
    <p class="pouch__descriptor">Herbal tea supplement</p>
    <p class="pouch__weight">50G</p>
  </section>
</body>
</html>
```